Need 3 posters for in-store display

Hi Marla,

Hope you are well.
I need 3 posters for display in my restaurant.

Poster 1: To be print in A1 size vertical
Title: BOWL-ERIFIC DEAL $19.50
Choose any Pho OR Noodle Salads
Choose Spring Rolls (5 rolls) OR Ricepaper Rolls (2 rolls)
Choose any Cans OR Water

What I like to see:
- These poster will be place near my counter so I want it to grab customer attention.
- You must use photos to show products
- Make it easy to understand and for customer to follow

Poster 2: To be print in A4 size vertical
Title: ADD TO YOUR ORDER
SpringRolls (Crab / vegetarian) $6 / 5 rolls
Extra Meat $2
Extra Noodles $1
Extra Vegs $1.5
Extra Tofu $2
Extra Crackling $3

Poster 3: To be print in A1 size vertical
Title: BROTH BONANZA FEAST
Catering Menu Options:
- PHO (Beef, Chicken, Vegan) $12.50 per bowl
- NOODLE SALADS (Beef, Chicken, BBQ Pork, Vegan) $12.50 per bowl
- SpringRolls (Crab / vegetarian) $12.50 for 10 rolls
- Ricepaper Rolls (Prawn, Beef, Chicken, BBQ Pork, Tofu) $12.5 / 5 rolls
- Fried Rice (Prawn, Tofu) $50 per tray (serve 5-6)

Terms & Conditions for All Catering Orders:
1) Minimum orders $200 (Pick-Up from shop Only)
2) All orders must be paid upfront
3) Requires $300 bond for Soup Tank
4) Please give us 48hours notice

• For the BOWL-ERIFIC DEAL
• it would be nice to have an image of the battle of water to visually complete the meal deal
• please see attachment of the Cedar Ridge Water

```html
<!DOCTYPE html>
<html lang="en">
<head>
<meta charset="utf-8">
<title>Bowl-erific Deal Poster</title>
<link rel="stylesheet" href="https://fonts.googleapis.com/css2?family=Open+Sans:wght@800&family=Montserrat:wght@500;600&display=swap">
<style>
  :root {
    --lime: #9ec41b;
    --white: #ffffff;
    --gold-light: #f2d27a;
    --gold: #d4a73c;
    --gold-dark: #a9801f;
    --ink: #111111;
    --footer-ink: #2b2b2b;
    --top-dark: #0e0e0d;
    --top-mid: #3b3a36;
    --wood-light: #7a5c40;
    --wood-dark: #3a2819;
    --photo-food: #c9bba6;
    --photo-bottle: #dfe7ee;
  }
  * { margin: 0; padding: 0; box-sizing: border-box; }
  html, body { width: 872px; height: 1200px; overflow: hidden; background: #ffffff; }
  .poster {
    position: relative;
    width: 872px;
    height: 1200px;
    overflow: hidden;
    background: linear-gradient(180deg, var(--top-mid) 0%, #2a2926 35%, var(--top-dark) 58%);
    font-family: "Montserrat", sans-serif;
  }
  .backdrop-photo {
    position: absolute; left: 0; top: 0; width: 872px; height: 640px;
    background: radial-gradient(ellipse at 70% 40%, rgba(150,150,140,0.3), transparent 60%),
                radial-gradient(ellipse at 25% 10%, rgba(120,110,100,0.3), transparent 55%);
  }
  .table-photo {
    position: absolute; left: 0; top: 630px; width: 872px; height: 505px;
    background: linear-gradient(180deg, var(--top-dark) 0%, var(--wood-dark) 18%, var(--wood-light) 60%, #6a4e35 100%);
  }
  .title {
    position: absolute; left: 80px; top: 52px;
    font-family: "Open Sans", sans-serif; font-weight: 800;
  }
  .title-main {
    color: var(--lime); font-size: 106px; line-height: 1; letter-spacing: -2px;
  }
  .title-row { display: flex; align-items: center; margin-top: 0; }
  .title-sub { color: var(--white); font-size: 88px; line-height: 1; letter-spacing: -2px; }
  .price-bar {
    margin-left: 16px; height: 58px; width: 340px;
    background: linear-gradient(90deg, var(--gold-dark), var(--gold) 40%, var(--gold-light) 80%, var(--gold));
    color: var(--ink); font-size: 72px; line-height: 58px; padding-left: 36px; letter-spacing: -1px;
    white-space: nowrap;
  }
  .choose-box {
    position: absolute; left: 97px; top: 289px; width: 680px; height: 329px;
  }
  .choose-frame { position: absolute; left: 0; top: 0; }
  .choose-label {
    position: absolute; left: 0; width: 680px; top: -26px; text-align: center;
    font-family: "Open Sans", sans-serif; font-weight: 800; font-size: 44px; line-height: 52px;
    color: var(--gold);
  }
  .divider {
    position: absolute; left: 316px; width: 2px; background: var(--gold);
  }
  .divider.upper { top: 56px; height: 96px; }
  .divider.lower { top: 200px; height: 94px; }
  .or-mark {
    position: absolute; left: 292px; top: 154px; width: 50px; text-align: center;
    color: var(--lime); font-size: 32px; font-weight: 500; line-height: 44px;
  }
  .option {
    position: absolute; color: var(--white); font-size: 31px; font-weight: 500; line-height: 1;
    white-space: nowrap;
  }
  .option small { display: block; font-size: 21px; margin-top: 10px; }
  .option.left { right: 416px; text-align: right; }
  .option.right { left: 365px; text-align: left; }
  .row-1 { top: 62px; }
  .row-2 { top: 135px; }
  .row-3 { top: 246px; }
  .food-photo {
    position: absolute; left: 104px; top: 728px; width: 530px; height: 366px;
    border-radius: 8px; background: var(--photo-food);
  }
  .bottle-photo {
    position: absolute; left: 644px; top: 637px; width: 136px; height: 420px;
    border-radius: 8px; background: var(--photo-bottle);
  }
  .footer {
    position: absolute; left: 0; top: 1135px; width: 872px; height: 65px;
    background: linear-gradient(90deg, var(--gold) 0%, var(--gold-light) 50%, var(--gold) 100%);
    display: flex; align-items: center; justify-content: space-between;
    padding: 0 44px 0 46px; color: var(--footer-ink); font-size: 23px; font-weight: 500;
  }
  .web { display: flex; align-items: center; gap: 12px; }
</style>
</head>
<body>
  <main class="poster">
    <div class="backdrop-photo" role="img" aria-label="Blurred close-up of fresh rice paper rolls and dipping sauce"></div>
    <div class="table-photo" role="img" aria-label="Rustic wooden tabletop"></div>

    <header class="title">
      <div class="title-main">BOWL-ERIFIC</div>
      <div class="title-row">
        <span class="title-sub">DEAL</span>
        <span class="price-bar">$19.50</span>
      </div>
    </header>

    <section class="choose-box">
      <svg class="choose-frame" width="680" height="329" viewBox="0 0 680 329" aria-hidden="true">
        <path d="M228,1 H21 A20,20 0 0 0 1,21 V308 A20,20 0 0 0 21,328 H659 A20,20 0 0 0 679,308 V21 A20,20 0 0 0 659,1 H452"
              fill="none" stroke="#d4a73c" stroke-width="2"/>
      </svg>
      <h2 class="choose-label">CHOOSE</h2>
      <div class="divider upper"></div>
      <div class="divider lower"></div>
      <div class="or-mark">OR</div>

      <div class="option left row-1">ANY PHO</div>
      <div class="option right row-1">NOODLE SALADS</div>
      <div class="option left row-2">SPRING ROLLS<small>(5 ROLLS)</small></div>
      <div class="option right row-2">RICEPAPER ROLLS<small>(2 ROLLS)</small></div>
      <div class="option left row-3">ANY CANS</div>
      <div class="option right row-3">WATER</div>
    </section>

    <div class="food-photo" role="img" aria-label="Three bowls of beef noodle salad with herbs and bean sprouts"></div>
    <div class="bottle-photo" role="img" aria-label="Bottle of Cedar Ridge Water"></div>

    <footer class="footer">
      <span class="phone">Call Us: 0400 555 218</span>
      <span class="web">
        <svg width="26" height="26" viewBox="0 0 26 26" aria-hidden="true">
          <circle cx="13" cy="13" r="12" fill="none" stroke="#2b2b2b" stroke-width="1.5"/>
          <circle cx="13" cy="13" r="8.5" fill="none" stroke="#2b2b2b" stroke-width="1.3"/>
          <ellipse cx="13" cy="13" rx="3.8" ry="8.5" fill="none" stroke="#2b2b2b" stroke-width="1.2"/>
          <line x1="4.5" y1="13" x2="21.5" y2="13" stroke="#2b2b2b" stroke-width="1.2"/>
          <line x1="6" y1="9" x2="20" y2="9" stroke="#2b2b2b" stroke-width="1"/>
          <line x1="6" y1="17" x2="20" y2="17" stroke="#2b2b2b" stroke-width="1"/>
        </svg>
        www.bowlerific.com.au
      </span>
    </footer>
  </main>
</body>
</html>
```